Thornfield Visa Group Business Card

Boston based immigration and tax law firm.
Will serve wealthy individuals who wish to immigrate to the US.
Colors as in Logo, blue white.
Delivering sophisticated legal services.
Attached please see logo design from website.
Target Market(s)
non-US citizens
Industry/Entity Type
Legal
Contact Information for Business Card
Gerald T. Hensworth, Esq. LL.M, M.Sc., M.Fin
Thornfield Visa Group LLC
47 Kessel Ave., #218
Boston, MA 02134
Boston +1 617 555 0143
London +44 20 7946 0381
Sydney +61 2 5550 1296
www.thornfieldvisagroup.example
ghensworth@thornfieldvisagroup.example
United States Immigration and Tax Counsel

```html
<!DOCTYPE html>
<html lang="en">
<head>
<meta charset="utf-8">
<title>Thornfield Visa Group – Business Card</title>
<link href="https://fonts.googleapis.com/css2?family=Oswald:wght@400;500;600&display=swap" rel="stylesheet">
<style>
  :root {
    --backdrop: #2b2b2d;
    --navy: #0f1c52;
    --navy-deep: #0a1440;
    --ink: #1a2a6c;
    --teal: #3a9cc8;
    --paper: #ffffff;
    --text: #3a3f55;
  }
  * { margin: 0; padding: 0; box-sizing: border-box; }
  html, body { width: 1200px; height: 588px; overflow: hidden; }
  body {
    background: var(--backdrop);
    position: relative;
    font-family: "Oswald", "Arial Narrow", sans-serif;
  }
  .card {
    position: absolute;
    top: 187px;
    width: 392px;
    height: 223px;
    border-radius: 14px;
    overflow: hidden;
  }
  /* Back side */
  .card-back {
    left: 157px;
    background: linear-gradient(135deg, var(--navy) 0%, var(--navy-deep) 100%);
  }
  .brand-back {
    position: absolute;
    left: 62px; top: 84px;
    display: flex; align-items: center; gap: 12px;
  }
  .brand-square {
    display: block;
    background: var(--teal);
  }
  .brand-back .brand-square { width: 52px; height: 52px; }
  .brand-back .brand-name {
    color: var(--paper);
    font-weight: 500;
    font-size: 27px;
    line-height: 1.1;
    letter-spacing: 0.5px;
  }
  .tagline {
    position: absolute;
    left: 0; right: 0; top: 186px;
    text-align: center;
    color: var(--teal);
    font-size: 11px;
    letter-spacing: 0.6px;
  }
  /* Front side */
  .card-front {
    left: 660px;
    background: var(--paper);
  }
  .brand-front {
    position: absolute;
    left: 28px; top: 28px;
    display: flex; align-items: center; gap: 10px;
  }
  .brand-front .brand-square { width: 34px; height: 34px; background: var(--ink); }
  .brand-front .brand-name {
    color: var(--ink);
    font-weight: 500;
    font-size: 22px;
    line-height: 1;
  }
  .holder {
    position: absolute;
    right: 25px; top: 127px;
    color: var(--ink);
    font-weight: 600;
    font-size: 12px;
  }
  .rule {
    position: absolute;
    left: 25px; right: 25px; top: 151px;
    height: 1px; background: var(--ink);
  }
  .contacts {
    position: absolute;
    top: 162px; left: 26px; right: 20px;
    font-size: 7.2px;
    line-height: 13px;
    color: var(--text);
  }
  .col { position: absolute; top: 0; }
  .col-address { left: 0; padding-left: 11px; }
  .col-offices { left: 126px; }
  .col-direct { left: 233px; }
  .label { color: var(--ink); font-weight: 600; }
  .office-row span:first-child { display: inline-block; width: 28px; }
  .icon-row { display: flex; align-items: center; gap: 5px; }
  .icon-row svg { width: 7px; height: 7px; fill: var(--ink); }
  .pin { position: absolute; left: 0; top: 2px; width: 7px; height: 9px; fill: var(--teal); }
  .footer-band {
    position: absolute; left: 0; right: 0; bottom: 0; height: 14px;
    background: linear-gradient(90deg, var(--teal) 0 40px, var(--ink) 40px calc(100% - 25px), var(--teal) calc(100% - 25px));
  }
</style>
</head>
<body>

  <section class="card card-back">
    <div class="brand-back">
      <span class="brand-square"></span>
      <span class="brand-name">Thornfield Visa Group</span>
    </div>
    <p class="tagline">UNITED STATES IMMIGRATION AND TAX COUNSEL</p>
  </section>

  <section class="card card-front">
    <div class="brand-front">
      <span class="brand-square"></span>
      <span class="brand-name">Thornfield Visa Group</span>
    </div>

    <p class="holder">Gerald T. Hensworth, Esq. LL.M, M.Sc., M.Fin</p>
    <div class="rule"></div>

    <div class="contacts">
      <div class="col col-address">
        <svg class="pin" viewBox="0 0 10 13"><path d="M5 0a5 5 0 0 0-5 5c0 3.5 5 8 5 8s5-4.5 5-8a5 5 0 0 0-5-5zm0 7a2 2 0 1 1 0-4 2 2 0 0 1 0 4z"/></svg>
        <div class="label">Thornfield Visa Group LLC</div>
        <div>47 Kessel Ave., #218</div>
        <div>Boston, MA 02134</div>
      </div>
      <div class="col col-offices">
        <div class="office-row"><span class="label">Boston</span><span>+1 617 555 0143</span></div>
        <div class="office-row"><span class="label">London</span><span>+44 20 7946 0381</span></div>
        <div class="office-row"><span class="label">Sydney</span><span>+61 2 5550 1296</span></div>
      </div>
      <div class="col col-direct">
        <div class="icon-row">
          <svg viewBox="0 0 10 10"><path d="M2 0l2 2.5-1.2 1.3a6 6 0 0 0 3.4 3.4L7.5 6 10 8l-1.5 2C4 10 0 6 0 1.5z"/></svg>
          <span>+1 617 555 0143</span>
        </div>
        <div class="icon-row">
          <svg viewBox="0 0 10 10"><path d="M0 2h10v1L5 6 0 3zm0 2.2l5 3 5-3V8H0z"/></svg>
          <span>ghensworth@thornfieldvisagroup.example</span>
        </div>
        <div class="icon-row">
          <svg viewBox="0 0 10 10"><circle cx="5" cy="5" r="5"/></svg>
          <span>www.thornfieldvisagroup.example</span>
        </div>
      </div>
    </div>

    <div class="footer-band"></div>
  </section>

</body>
</html>
```